Real Estate Business Cards

Looking for a clean, sharp and professional look for our Real Estate investment Fund that invests in Multi Family Apartment buildings.

Target Market(s)

Real Estate Fund

Industry/Entity Type

Real Estate

Contact Information for Business Card

Company Description: Real Estate Investment Fund
Company Name: RKW Holdings
Name: Marcus Olvane
Cell: (917) 482-0657
Email: marcus@rkwholdings-example.com
Website: www.rkwholdings-example.com
Address: 418, 9th Street, Brooklyn NY 11218

Colors

Designer to choose colors to be used in the design.

Requirements
Nice to have
• Colors to match logo

```html
<!DOCTYPE html>
<html lang="en">
<head>
<meta charset="UTF-8">
<title>RKW Holdings — Business Card</title>
<link href="https://fonts.googleapis.com/css2?family=Bebas+Neue&family=Montserrat:wght@400;500&display=swap" rel="stylesheet">
<style>
  :root {
    --brand-blue: #0d6aa2;
    --brand-blue-deep: #0a5283;
    --card-white: #ffffff;
    --ink: #2b2b2b;
    --backdrop: #e4e6e9;
    --mark-light: #dfe4ea;
  }
  * { margin: 0; padding: 0; box-sizing: border-box; }
  html, body {
    width: 1200px; height: 900px; overflow: hidden;
    background: var(--backdrop);
    font-family: "Montserrat", sans-serif;
  }
  .sheet {
    width: 1200px; height: 900px;
    display: flex; flex-direction: column;
    align-items: center; justify-content: center; gap: 50px;
  }
  .card {
    width: 600px; height: 343px;
    position: relative;
    box-shadow: 0 10px 28px rgba(0,0,0,0.18);
  }
  /* Front */
  .card-front {
    background: radial-gradient(ellipse at 55% 55%, #ffffff 0%, #f3f3f3 100%);
  }
  .holder-name {
    position: absolute; left: 36px; top: 112px;
    width: 250px;
    font-family: "Bebas Neue", sans-serif;
    font-weight: 400;
    font-size: 50px; line-height: 1;
    color: var(--brand-blue);
    letter-spacing: 0.5px;
    white-space: nowrap;
  }
  .divider {
    position: absolute; left: 298px; top: 102px;
    width: 2px; height: 72px;
    background: var(--brand-blue);
  }
  .contact-list {
    position: absolute; left: 314px; top: 102px;
    list-style: none;
    font-size: 12px; color: var(--ink);
  }
  .contact-list li {
    display: flex; align-items: center; gap: 8px;
    height: 24px;
    white-space: nowrap;
  }
  .contact-list svg { width: 12px; height: 12px; flex: none; }
  .contact-list .accent { color: var(--brand-blue); }
  .address {
    position: absolute; left: 36px; top: 232px;
    display: flex; align-items: center; gap: 8px;
    font-size: 13px; color: var(--ink);
    white-space: nowrap;
  }
  .address svg { width: 12px; height: 14px; flex: none; }
  /* Back */
  .card-back {
    background: linear-gradient(135deg, var(--brand-blue) 0%, var(--brand-blue-deep) 100%);
    display: flex; align-items: center; justify-content: center; gap: 16px;
  }
  .back-square {
    width: 28px; height: 28px;
    background: var(--mark-light);
  }
  .company-name {
    font-family: "Montserrat", sans-serif;
    font-weight: 500;
    font-size: 40px;
    letter-spacing: 3px;
    text-transform: uppercase;
    color: var(--mark-light);
  }
</style>
</head>
<body>
<main class="sheet">
  <section class="card card-front" aria-label="Card front">
    <h1 class="holder-name">Marcus Olvane</h1>
    <div class="divider"></div>
    <ul class="contact-list">
      <li>
        <svg viewBox="0 0 24 24" fill="var(--brand-blue)"><path d="M6.6 10.8a15.1 15.1 0 006.6 6.6l2.2-2.2a1 1 0 011-.25 11.4 11.4 0 003.6.57 1 1 0 011 1V20a1 1 0 01-1 1A17 17 0 013 4a1 1 0 011-1h3.5a1 1 0 011 1c0 1.25.2 2.45.57 3.57a1 1 0 01-.25 1z"/></svg>
        <span>(917) 482-0657</span>
      </li>
      <li>
        <svg viewBox="0 0 24 24" fill="none" stroke="var(--brand-blue)" stroke-width="2.4"><rect x="2" y="5" width="20" height="14"/><path d="M2 5l10 8 10-8"/></svg>
        <span>marcus@rkwholdings-example.com</span>
      </li>
      <li>
        <svg viewBox="0 0 24 24" fill="none" stroke="var(--brand-blue)" stroke-width="2"><circle cx="12" cy="12" r="10"/><path d="M2 12h20M12 2c3 3 3 17 0 20M12 2c-3 3-3 17 0 20"/></svg>
        <span>www.<span class="accent">rkwholdings-example</span>.com</span>
      </li>
    </ul>
    <p class="address">
      <svg viewBox="0 0 24 28" fill="var(--brand-blue)"><path d="M12 0a10 10 0 00-10 10c0 7.5 10 18 10 18s10-10.5 10-18A10 10 0 0012 0zm0 14a4 4 0 110-8 4 4 0 010 8z"/></svg>
      <span>418, 9th Street, Brooklyn NY 11218</span>
    </p>
  </section>

  <section class="card card-back" aria-label="Card back">
    <div class="back-square"></div>
    <p class="company-name">RKW Holdings</p>
  </section>
</main>
</body>
</html>
```